Lumenfield Holdings

Professional looking business card using darker colours
I do not yet have a logo for the company so feel free to suggest
The business is based on consultancy and project management
Based in Melbourne
Business card can omit the word "Holdings" and can be Lumenfield consulting etc.

Business

Contact Name on card : Tom Verisco Contact number : +61412 305 617 Email address will be confirmed shortly.

```html
<!DOCTYPE html>
<html lang="en">
<head>
<meta charset="utf-8">
<title>Lumenfield Consulting – Business Card</title>
<link rel="stylesheet" href="https://fonts.googleapis.com/css2?family=Michroma&family=Roboto:wght@700&family=Roboto+Condensed:ital,wght@0,400;1,400&family=Fira+Sans:wght@400&display=swap">
<style>
  :root {
    --card-bg: #360b26;
    --ink: #ffffff;
    --glow: #e9d9e3;
    --mauve: #8a5a78;
    --label: #4a4a4a;
    --page: #ffffff;
  }
  * { margin: 0; padding: 0; box-sizing: border-box; }
  html, body { width: 977px; height: 1200px; overflow: hidden; background: var(--page); }
  .canvas { position: relative; width: 977px; height: 1200px; }

  .side-label {
    position: absolute;
    font-family: "Fira Sans", sans-serif;
    font-size: 36px;
    color: var(--label);
    letter-spacing: 1px;
    text-shadow: 0 0 2px rgba(0,0,0,.25);
  }
  .side-label span { margin-left: 44px; }
  .label-front { left: 220px; top: 10px; }
  .label-back  { left: 189px; top: 615px; }

  .card {
    position: absolute;
    left: 33px;
    width: 926px;
    height: 525px;
    background: var(--card-bg);
    overflow: hidden;
  }
  .card-front { top: 66px; }
  .card-back  { top: 662px; }

  .line-texture {
    position: absolute; left: 0; top: 0; width: 210px; height: 525px;
    background: radial-gradient(ellipse 180px 340px at 20px 300px, rgba(200,160,185,.16), rgba(200,160,185,0) 100%);
  }
  .orb {
    position: absolute;
    border-radius: 50%;
  }
  .orb-front {
    left: 70px; top: 86px; width: 210px; height: 210px;
    background: radial-gradient(circle at 55% 40%, var(--glow) 0%, var(--mauve) 45%, rgba(54,11,38,0) 72%);
  }
  .orb-back {
    left: 560px; top: -20px; width: 520px; height: 520px;
    background: radial-gradient(circle at 62% 50%, var(--glow) 0%, #a57b95 28%, #6a3658 52%, rgba(54,11,38,0) 72%);
  }

  .holding-name {
    position: absolute;
    font-family: "Roboto", sans-serif;
    font-weight: 700;
    color: var(--ink);
    letter-spacing: .5px;
    line-height: 1.05;
  }
  .holding-front { left: 26px; top: 268px; font-size: 26px; }
  .holding-back  { left: 88px; top: 224px; font-size: 26px; }
  .holding-mark {
    display: inline-block; width: 18px; height: 18px; border-radius: 50%;
    background: var(--ink); margin-right: 8px; vertical-align: 1px;
  }

  .wordmark { position: absolute; left: 311px; top: 150px; }

  .person { position: absolute; left: 53px; top: 400px; color: var(--ink); }
  .person-name { font-family: "Roboto", sans-serif; font-weight: 700; font-size: 32px; }
  .person-role { font-family: "Roboto Condensed", sans-serif; font-size: 29px; margin-top: 2px; }

  .contact { position: absolute; right: 81px; top: 402px; text-align: right; color: var(--ink); font-family: "Roboto Condensed", sans-serif; }
  .contact-tel { font-size: 35px; }
  .contact-email { font-style: italic; font-size: 22px; margin-top: 6px; }

  .divider { position: absolute; left: 295px; top: 226px; width: 2px; height: 116px; background: var(--ink); opacity: .9; }
  .tagline {
    position: absolute; left: 313px; top: 240px;
    font-family: "Roboto", sans-serif; font-weight: 700; font-size: 35px;
    color: var(--ink); line-height: 44px;
  }
</style>
</head>
<body>
<div class="canvas">

  <div class="side-label label-front">Front<span>A</span></div>

  <section class="card card-front">
    <div class="line-texture" role="img" aria-label="Fine flowing line texture"></div>
    <div class="orb orb-front" role="img" aria-label="Glowing globe decoration"></div>
    <div class="holding-name holding-front"><span class="holding-mark"></span>LUMENFIELD<br>HOLDINGS</div>

    <svg class="wordmark" width="570" height="90" viewBox="0 0 570 90">
      <text x="0" y="55" font-family="Michroma, sans-serif" font-size="50" fill="#ffffff" textLength="562" lengthAdjust="spacingAndGlyphs">LUMENFIELD</text>
      <line x1="0" y1="66" x2="563" y2="66" stroke="#ffffff" stroke-width="2"/>
      <text x="237" y="88" font-family="Michroma, sans-serif" font-size="14" fill="#ffffff" textLength="326" lengthAdjust="spacing">CONSULTING</text>
    </svg>

    <div class="person">
      <div class="person-name">Tom Verisco</div>
      <div class="person-role">Director</div>
    </div>

    <div class="contact">
      <div class="contact-tel">Tel: +61412 305 617</div>
      <div class="contact-email">Email:Tomverisco@lumenfield.com</div>
    </div>
  </section>

  <div class="side-label label-back">Back<span>A</span></div>

  <section class="card card-back">
    <div class="orb orb-back" role="img" aria-label="Large glowing globe decoration"></div>
    <div class="holding-name holding-back"><span class="holding-mark"></span>LUMENFIELD<br>HOLDINGS</div>
    <div class="divider"></div>
    <div class="tagline">Business Consultancy<br>And Management</div>
  </section>

</div>
</body>
</html>
```